1 Cup Pod - Regular and Decaf

I am looking for 2 package designs. When you open the uploaded file it show one for regular and one for decaf. The size is also on the example template. Both products with still be named Café Tovami, only things we are looking for is new colors and design of package. you can use up to 4 colors at this time.

We are open to all types of ideas and colors. the only thins is the regular and decaf must be different colors.

Requirements
Must have
• Must use the exact information used on front and back of both package design from the example template. The only thing is to add, 48391 next to where it says Brenwick, TX

```html
<!DOCTYPE html>
<html lang="en">
<head>
<meta charset="utf-8">
<title>Café Tovami – Single-Cup Coffee Pod Packaging</title>
<link rel="stylesheet" href="https://fonts.googleapis.com/css2?family=Alegreya:wght@700&family=Alegreya+Sans:wght@700&family=Marcellus&display=swap">
<style>
  :root {
    --page: #2d1d0e;
    --roast: #7a5530;
    --roast-deep: #6a4826;
    --roast-badge: #8a6239;
    --gold: #e8c24a;
    --gold-soft: #e5c352;
    --tan: #c18c4b;
    --tan-text: #94713f;
    --cream: #fff7df;
    --ink: #3a2613;
    --burlap-a: #b9aa94;
    --burlap-b: #8f7f69;
  }
  * { box-sizing: border-box; margin: 0; padding: 0; }
  html, body {
    width: 1148px; height: 1200px; overflow: hidden;
    background: var(--page);
  }
  .pack {
    position: absolute; left: 24px; width: 1093px; height: 547px;
    font-family: "Alegreya", Georgia, serif; font-weight: 700;
    overflow: hidden;
  }
  .pack--regular { top: 33px; background: var(--roast); }
  .pack--decaf   { top: 619px; background: var(--gold-soft); }

  .pack__topbar {
    position: absolute; left: 0; top: 0; width: 100%; height: 43px;
    font-size: 21px; line-height: 43px;
  }
  .pack__type { position: absolute; left: 13px; top: 2px; }
  .pack__origin { position: absolute; left: 396px; top: -2px; }
  .pack--regular .pack__type { color: var(--cream); }
  .pack--regular .pack__origin { color: var(--gold); }
  .pack--decaf .pack__type { color: var(--ink); }
  .pack--decaf .pack__origin { color: var(--tan-text); }

  .pack__burlap {
    position: absolute; left: 0; top: 43px; width: 100%; height: 428px;
    background: linear-gradient(135deg, var(--burlap-a), var(--burlap-b) 50%, var(--burlap-a));
  }

  .pack__weight {
    position: absolute; left: 468px; top: 39px; width: 38px; height: 38px;
    border-radius: 50%; text-align: center; line-height: 38px;
    font-size: 22px; color: var(--ink);
  }
  .pack__weight small { font-size: 15px; }
  .pack--regular .pack__weight { background: var(--gold); }
  .pack--decaf .pack__weight { background: var(--gold-soft); }

  .brand {
    position: absolute; left: 76px; top: 53px; width: 374px; height: 374px;
    border-radius: 50%;
    display: flex; flex-direction: column; align-items: center; justify-content: center;
    font-family: "Marcellus", Georgia, serif; font-weight: 400;
    font-size: 68px; line-height: 1.0; text-align: center;
  }
  .pack--regular .brand { background: var(--roast-badge); color: var(--gold); }
  .pack--decaf .brand { background: var(--tan); color: var(--cream); }

  .directions {
    position: absolute; left: 625px; top: 47px; width: 378px; height: 424px;
    border-radius: 26px / 40px;
    text-align: center; font-size: 20px; line-height: 34.7px;
    padding-top: 26px;
  }
  .pack--regular .directions { background: var(--roast); color: var(--cream); }
  .pack--decaf .directions { background: var(--gold-soft); color: var(--ink); }
  .directions__maker {
    margin-top: 59px; font-size: 23px; line-height: 28px;
  }
  .pack--regular .directions__maker { color: var(--gold); }
  .pack--decaf .directions__maker { color: var(--tan-text); }

  .pack__band {
    position: absolute; left: 0; top: 471px; width: 100%; height: 76px;
  }
  .pack--regular .pack__band { background: var(--roast-deep); }
  .pack--decaf .pack__band { background: var(--gold-soft); }
  .pack__stitch {
    position: absolute; left: 0; top: 10px; width: 100%; height: 3px;
  }
  .pack__label {
    position: absolute; left: 0; top: 20px; width: 400px; text-align: center;
    font-family: "Alegreya Sans", Arial, sans-serif; font-weight: 700;
    font-size: 33px; letter-spacing: 2px; line-height: 40px;
  }
  .pack--regular .pack__label { color: var(--gold); left: 0; width: 358px; }
  .pack--decaf .pack__label { color: var(--roast); left: 0; width: 448px; }
</style>
</head>
<body>

<section class="pack pack--regular">
  <div class="pack__burlap" role="img" aria-label="Woven burlap coffee sack texture"></div>
  <div class="pack__topbar">
    <span class="pack__type">Single-Cup Coffee Pod</span>
    <span class="pack__origin">Colombian</span>
  </div>
  <div class="pack__weight">7<small>gr</small></div>
  <div class="brand"><span>CAFÉ</span><span>TOVAMI</span></div>
  <div class="directions">
    <p>DIRECTIONS;</p>
    <p>Carefully open package.</p>
    <p>DO NOT OPEN FILTER PACK</p>
    <p>Place single-cup coffee pod</p>
    <p>in brew basket or funnel.</p>
    <p>Follow the directions on</p>
    <p>your coffee maker</p>
    <p class="directions__maker">MERIDOR &amp; SONS<br>Brenwick, Texas, 48391</p>
  </div>
  <div class="pack__band">
    <svg class="pack__stitch" viewBox="0 0 1093 3" preserveAspectRatio="none">
      <line x1="0" y1="1.5" x2="1093" y2="1.5" stroke="#b5864a" stroke-width="3" stroke-dasharray="22 12"/>
    </svg>
    <div class="pack__label">REGULAR</div>
  </div>
</section>

<section class="pack pack--decaf">
  <div class="pack__burlap" role="img" aria-label="Woven burlap coffee sack texture"></div>
  <div class="pack__topbar">
    <span class="pack__type">Single-Cup Coffee Pod</span>
    <span class="pack__origin">Colombian</span>
  </div>
  <div class="pack__weight">7<small>gr</small></div>
  <div class="brand"><span>CAFÉ</span><span>TOVAMI</span></div>
  <div class="directions">
    <p>DIRECTIONS;</p>
    <p>Carefully open package.</p>
    <p>DO NOT OPEN FILTER PACK</p>
    <p>Place single-cup coffee pod</p>
    <p>in brew basket or funnel.</p>
    <p>Follow the directions on</p>
    <p>your coffee maker</p>
    <p class="directions__maker">MERIDOR &amp; SONS<br>Brenwick, Texas, 48391</p>
  </div>
  <div class="pack__band">
    <svg class="pack__stitch" viewBox="0 0 1093 3" preserveAspectRatio="none">
      <line x1="0" y1="1.5" x2="1093" y2="1.5" stroke="#b8924a" stroke-width="3" stroke-dasharray="22 12"/>
    </svg>
    <div class="pack__label">DECAFFEINATED</div>
  </div>
</section>

</body>
</html>
```